Banner Design

We need a vinyl outside banner designed to be printed for Corvale University Residential Communities, based in Sydney. Our product is colleges and apartments for students. Our target market are students that are not currently living on campus and have long journeys. We need the message "You could be home right now" to be displayed. This would be displayed at bus stops where students are waiting in long lines to get home, when it's cold outside and they have a long journey ahead. The final design should be clear, concise and communicate the convenience of living on campus. Size is 3m wide by 1m high with 2 inch border around the design.

```html
<!DOCTYPE html>
<html lang="en">
<head>
<meta charset="UTF-8">
<title>Corvale University Residential Communities – Bus Stop Banner</title>
<link rel="stylesheet" href="https://fonts.googleapis.com/css2?family=Barlow+Semi+Condensed:wght@700&display=swap">
<style>
  :root {
    --banner-yellow: #fcd307;
    --ink: #231f20;
    --backdrop: #ffffff;
    --photo-tone-light: #ece6dc;
    --photo-tone-mid: #d9cfc1;
  }
  * { margin: 0; padding: 0; box-sizing: border-box; }
  html, body {
    width: 1200px;
    height: 400px;
    overflow: hidden;
    background: var(--backdrop);
  }
  .banner {
    position: relative;
    width: 1200px;
    height: 400px;
    background: var(--backdrop);
    font-family: "Barlow Semi Condensed", "Arial Narrow", sans-serif;
    font-weight: 700;
    color: var(--ink);
  }
  .banner__panel {
    position: absolute;
    left: 10px;
    top: 10px;
    width: 1032px;
    height: 378px;
    background: var(--banner-yellow);
  }
  .brand {
    position: absolute;
    left: 70px;
    top: 128px;
    width: 210px;
    display: flex;
    flex-direction: column;
    align-items: center;
  }
  .brand__mark {
    width: 72px;
    height: 72px;
    background: var(--ink);
    margin-bottom: 30px;
  }
  .brand__name {
    font-size: 54px;
    line-height: 0.9;
    letter-spacing: 0.5px;
    text-transform: uppercase;
  }
  .brand__sub {
    font-size: 17px;
    line-height: 1;
    margin-top: 10px;
    letter-spacing: 4px;
    text-transform: uppercase;
  }
  .headline {
    position: absolute;
    left: 388px;
    top: 130px;
    font-size: 74px;
    line-height: 66px;
    letter-spacing: 2.6px;
    text-transform: uppercase;
  }
  .students-photo {
    position: absolute;
    left: 1030px;
    top: 30px;
    width: 165px;
    height: 355px;
    background: linear-gradient(180deg, var(--photo-tone-light) 0%, var(--photo-tone-mid) 100%);
  }
</style>
</head>
<body>
  <main class="banner">
    <div class="banner__panel"></div>

    <div class="brand">
      <div class="brand__mark"></div>
      <span class="brand__name">Corvale</span>
      <span class="brand__sub">University</span>
    </div>

    <h1 class="headline">You could be<br>home right now</h1>

    <div class="students-photo" role="img" aria-label="Photo of three smiling students peeking around the right edge of the yellow panel"></div>
  </main>
</body>
</html>
```